CD Cover Design for Americana Rock EP Paper Lanterns

We need a CD cover design for an upcoming EP by TW Banfield titled Paper Lanterns. Although the cover should reflect the name of the title track, it should also be consistent with the overall sound of the EP and TW's brand. The EP, however, is a little more rock and a little less Americana that TW's previous EP, Cold Mill Creek.

Please review TW's website at www.twbanfield.net and listen to the attached preview tracks.

```html
<!DOCTYPE html>
<html lang="en">
<head>
<meta charset="utf-8">
<title>Paper Lanterns — TW Banfield EP Cover</title>
<link rel="stylesheet" href="https://fonts.googleapis.com/css2?family=Oswald:wght@500;600&display=swap">
<style>
  :root {
    --stage: #9fa3a4;
    --night: #120608;
    --maroon: #3a0a10;
    --ember: #8c1414;
    --flame: #e8611a;
    --flame-core: #f6a828;
    --title-ink: #f3d27a;
    --artist-ink: #f0b24a;
  }
  html, body {
    margin: 0;
    width: 1200px;
    height: 900px;
    overflow: hidden;
    background: var(--stage);
  }
  .canvas {
    position: relative;
    width: 1200px;
    height: 900px;
    display: flex;
    align-items: center;
    justify-content: center;
  }
  .ep-cover {
    position: relative;
    width: 820px;
    height: 820px;
    overflow: hidden;
    background: var(--night);
  }
  .cover-artwork {
    position: absolute;
    inset: 0;
    background:
      radial-gradient(ellipse 30% 22% at 6% 52%, rgba(230, 40, 60, 0.75), transparent 70%),
      radial-gradient(ellipse 55% 40% at 52% 48%, var(--flame-core), var(--flame) 35%, transparent 72%),
      radial-gradient(ellipse 45% 35% at 60% 90%, var(--flame), transparent 70%),
      linear-gradient(180deg, var(--night) 0%, var(--maroon) 28%, var(--ember) 55%, var(--maroon) 85%, var(--night) 100%);
  }
  .ep-title {
    position: absolute;
    top: 8.5%;
    left: 0;
    right: 0;
    margin: 0;
    text-align: center;
    font-family: "Oswald", sans-serif;
    font-weight: 600;
    font-size: 78px;
    letter-spacing: 4px;
    line-height: 1;
    text-transform: uppercase;
    color: var(--title-ink);
  }
  .artist-name {
    position: absolute;
    top: 89.5%;
    left: 0;
    right: 0;
    margin: 0;
    text-align: center;
    font-family: "Oswald", sans-serif;
    font-weight: 500;
    font-size: 28px;
    letter-spacing: 3px;
    line-height: 1;
    text-transform: uppercase;
    color: var(--artist-ink);
  }
</style>
</head>
<body>
  <main class="canvas">
    <section class="ep-cover">
      <div class="cover-artwork" role="img" aria-label="Cover artwork: silhouetted figure raising a knife in front of a wall of fire under a red night sky with a glowing moon, beside a second figure in round glasses"></div>
      <h1 class="ep-title">Paper Lanterns</h1>
      <p class="artist-name">TW Banfield</p>
    </section>
  </main>
</body>
</html>
```